Cell phone repair

you can please design me business card

size 3.5" x 2"

colors blue and red

fixit rapid logo (you get from my website fixitrapidco.example )

"We Come To You!

It is very simple! You tell us what phone you have, And we come to fix it."

phone number: 555.248.3906

website: www.fixitrapidco.example

email: info@fixitrapidco.example

```html
<!DOCTYPE html>
<html lang="en">
<head>
<meta charset="utf-8">
<title>Fixit Rapid – Business Cards</title>
<link rel="stylesheet" href="https://fonts.googleapis.com/css2?family=Arvo:wght@700&family=Gochi+Hand&family=Roboto:wght@500&display=swap">
<style>
  :root {
    --page: #ffffff;
    --card-grey: #e4e4e8;
    --card-grey-dark: #c9c9cf;
    --navy: #1d1a4d;
    --plum: #7a1a58;
    --ink: #0b0a10;
    --icon: #7d44c8;
    --brand-blue: #1a6fd1;
    --brand-red: #e52420;
    --tagline: #1f1f24;
    --white: #ffffff;
  }
  html, body {
    margin: 0;
    width: 927px;
    height: 1200px;
    overflow: hidden;
    background: var(--page);
  }
  .canvas { position: relative; width: 927px; height: 1200px; }
  .business-card {
    position: absolute;
    width: 392px;
    height: 224px;
    display: block;
  }
  .card-front { left: 50px; top: 40px; }
  .card-alt { left: 482px; top: 207px; }
  .headline { font-family: "Arvo", Georgia, serif; font-weight: 700; font-size: 13.5px; fill: var(--white); }
  .brand-name { font-family: "Roboto", Arial, sans-serif; font-weight: 500; font-size: 20px; fill: var(--brand-blue); }
  .tagline { font-family: "Gochi Hand", cursive; font-size: 12.5px; fill: var(--tagline); text-anchor: middle; }
  .contact { font-family: "Arvo", Georgia, serif; font-weight: 700; font-size: 5.8px; fill: var(--white); }
</style>
</head>
<body>
<main class="canvas">

  <!-- Card: desk phone version -->
  <svg class="business-card card-front" viewBox="0 0 360 205" aria-label="Fixit Rapid business card">
    <defs>
      <linearGradient id="barA" x1="0" x2="1"><stop offset="0" stop-color="var(--navy)"/><stop offset="1" stop-color="var(--plum)"/></linearGradient>
      <linearGradient id="greyA" x1="0" y1="0" x2="1" y2="1"><stop offset="0" stop-color="var(--card-grey)"/><stop offset="0.5" stop-color="var(--card-grey-dark)"/><stop offset="1" stop-color="var(--card-grey)"/></linearGradient>
      <linearGradient id="deviceA" x1="0" y1="0" x2="1" y2="1"><stop offset="0" stop-color="#8c8c94"/><stop offset="0.5" stop-color="#2a2a30"/><stop offset="1" stop-color="#4a4a58"/></linearGradient>
    </defs>
    <rect class="card-backdrop" width="360" height="205" fill="url(#greyA)"/>
    <polygon class="corner-bar" points="0,0 85,0 78,11 0,11" fill="url(#barA)"/>
    <polygon class="headline-banner" points="186,0 360,0 360,26 196,26" fill="url(#barA)"/>
    <text class="headline" x="206" y="18">"We Come To You!</text>

    <text class="brand-name" x="10" y="65">Fixit Rapid</text>
    <circle class="brand-dot" cx="160" cy="58" r="12" fill="var(--brand-red)"/>

    <text class="tagline" x="270" y="52">It is very simple!</text>
    <text class="tagline" x="270" y="67">You tell us what phone you have,</text>
    <text class="tagline" x="270" y="82">And we come to fix it."</text>

    <polygon class="accent-bar" points="0,98 170,98 178,108 0,108" fill="url(#barA)"/>
    <polygon class="contact-panel" points="0,108 300,108 310,118 360,118 360,205 0,205" fill="var(--ink)"/>
    <polygon class="base-bar" points="0,192 222,192 230,205 0,205" fill="url(#barA)"/>

    <rect class="device-photo" role="img" aria-label="Photo of a touchscreen smartphone with a cracked screen" x="252" y="88" width="102" height="117" rx="8" fill="url(#deviceA)"/>

    <g class="contact-row">
      <circle cx="28" cy="132" r="7" fill="var(--icon)"/>
      <path d="M25 128.5 q-1 3 3 7 q4 4 7 3 l-1.5-2 -2 .8 q-3-1.5-4.5-4.5 l.8-2z" fill="var(--white)"/>
      <text class="contact" x="40" y="134">555.248.3906</text>
      <circle cx="104" cy="132" r="7" fill="var(--icon)"/>
      <rect x="100" y="129" width="8" height="6" fill="var(--white)"/>
      <path d="M100 129 l4 3.5 4-3.5" fill="none" stroke="var(--icon)" stroke-width=".8"/>
      <text class="contact" x="116" y="134">email: info@fixitrapidco.example</text>
    </g>
    <g class="contact-row">
      <circle cx="28" cy="164" r="7" fill="var(--icon)"/>
      <g fill="none" stroke="var(--white)" stroke-width=".8">
        <circle cx="28" cy="164" r="4"/>
        <ellipse cx="28" cy="164" rx="1.8" ry="4"/>
        <path d="M24 164h8"/>
      </g>
      <text class="contact" x="40" y="166">web: www.fixitrapidco.example</text>
    </g>
  </svg>

  <!-- Card: hand-held phone version -->
  <svg class="business-card card-alt" viewBox="0 0 360 205" aria-label="Fixit Rapid business card, alternate">
    <defs>
      <linearGradient id="barB" x1="0" x2="1"><stop offset="0" stop-color="var(--navy)"/><stop offset="1" stop-color="var(--plum)"/></linearGradient>
      <linearGradient id="greyB" x1="0" y1="0" x2="1" y2="1"><stop offset="0" stop-color="var(--card-grey)"/><stop offset="0.5" stop-color="var(--card-grey-dark)"/><stop offset="1" stop-color="var(--card-grey)"/></linearGradient>
      <linearGradient id="deviceB" x1="0" y1="0" x2="1" y2="1"><stop offset="0" stop-color="#d9d9de"/><stop offset="0.45" stop-color="#3a3a42"/><stop offset="1" stop-color="#b88a70"/></linearGradient>
    </defs>
    <rect class="card-backdrop" width="360" height="205" fill="url(#greyB)"/>
    <polygon class="corner-bar" points="0,0 85,0 78,11 0,11" fill="url(#barB)"/>
    <polygon class="headline-banner" points="186,0 360,0 360,26 196,26" fill="url(#barB)"/>
    <text class="headline" x="206" y="18">"We Come To You!</text>

    <text class="brand-name" x="10" y="65">Fixit Rapid</text>
    <circle class="brand-dot" cx="160" cy="58" r="12" fill="var(--brand-red)"/>

    <text class="tagline" x="270" y="52">It is very simple!</text>
    <text class="tagline" x="270" y="67">You tell us what phone you have,</text>
    <text class="tagline" x="270" y="82">And we come to fix it."</text>

    <polygon class="accent-bar" points="0,98 170,98 178,108 0,108" fill="url(#barB)"/>
    <polygon class="contact-panel" points="0,108 300,108 310,118 360,118 360,205 0,205" fill="var(--ink)"/>
    <polygon class="base-bar" points="0,192 222,192 230,205 0,205" fill="url(#barB)"/>

    <rect class="device-photo" role="img" aria-label="Photo of a hand holding a smartphone with a shattered screen" x="242" y="92" width="118" height="110" rx="8" fill="url(#deviceB)"/>

    <g class="contact-row">
      <circle cx="28" cy="132" r="7" fill="var(--icon)"/>
      <path d="M25 128.5 q-1 3 3 7 q4 4 7 3 l-1.5-2 -2 .8 q-3-1.5-4.5-4.5 l.8-2z" fill="var(--white)"/>
      <text class="contact" x="40" y="134">555.248.3906</text>
      <circle cx="104" cy="132" r="7" fill="var(--icon)"/>
      <rect x="100" y="129" width="8" height="6" fill="var(--white)"/>
      <path d="M100 129 l4 3.5 4-3.5" fill="none" stroke="var(--icon)" stroke-width=".8"/>
      <text class="contact" x="116" y="134">email: info@fixitrapidco.example</text>
    </g>
    <g class="contact-row">
      <circle cx="28" cy="164" r="7" fill="var(--icon)"/>
      <g fill="none" stroke="var(--white)" stroke-width=".8">
        <circle cx="28" cy="164" r="4"/>
        <ellipse cx="28" cy="164" rx="1.8" ry="4"/>
        <path d="M24 164h8"/>
      </g>
      <text class="contact" x="40" y="166">web: www.fixitrapidco.example</text>
    </g>
  </svg>

</main>
</body>
</html>
```